Harborlight Behavioral and Community Services

Intellectual Developmental Disabilities, Group Homes, Residential Homes and Substance Abuse Residential facilities

Target Market(s)

Adults 18-59 male and female autism, developmental disabilities and mental health

Industry/Entity Type

Intellectual Development Disabilities, Autism, Applied Behavioral Analysis, Mental Health, Substance Abuse

Coding

Coded - Design and coding required

Number of Pages Required

5+ page

Font styles to use
Serif

Colors
0054AA
0677BA
7BADD7
CADEEF
E8F1F8

Requirements
Should not have
• Not specified

```html
<!DOCTYPE html>
<html lang="en">
<head>
<meta charset="utf-8">
<title>Harborlight Community Programs</title>
<link href="https://fonts.googleapis.com/css2?family=DM+Serif+Text&family=Inter:wght@400;500;600;700&display=swap" rel="stylesheet">
<style>
:root{
  --blue-deep:#0054AA;
  --blue-mid:#0677BA;
  --blue-soft:#7BADD7;
  --blue-pale:#CADEEF;
  --blue-mist:#E8F1F8;
  --bar:#1C62AF;
  --accent:#E6EA55;
  --white:#ffffff;
}
*{box-sizing:border-box;margin:0;padding:0}
html,body{width:1200px;height:3125px;overflow:hidden}
body{position:relative;background:var(--blue-mist);font-family:'Inter',sans-serif;color:var(--blue-deep)}
.abs{position:absolute}
.serif{font-family:'DM Serif Text',serif;font-weight:400}
.eyebrow{font-size:10px;font-weight:600;letter-spacing:.2px;text-transform:uppercase}
.pill{display:flex;align-items:center;justify-content:center;border-radius:20px;font-size:11px;font-weight:600}
.pill.soft{background:var(--blue-pale);color:var(--blue-deep)}
.pill.solid{background:var(--blue-mid);color:var(--white)}
.circle-btn{border-radius:50%;display:flex;align-items:center;justify-content:center}

/* header */
.site-header{left:0;top:0;width:1200px;height:62px;background:var(--blue-mist)}
.brand{left:194px;top:19px;display:flex;align-items:center;gap:7px}
.brand-dot{width:24px;height:24px;border-radius:50%;background:var(--blue-deep)}
.brand-name{font-family:'DM Serif Text',serif;font-size:10px;line-height:11px;color:var(--blue-deep)}
.nav{left:482px;top:25px;display:flex;gap:20px;font-size:9.5px;color:var(--blue-deep)}
.cta-top{left:890px;top:20px;width:116px;height:23px;padding:0 2px 0 10px;justify-content:space-between;font-weight:500;font-size:10px}
.cta-top .circle-btn{width:19px;height:19px;border:1px solid var(--white)}

/* hero */
.hero{left:0;top:62px;width:1200px;height:412px;background:linear-gradient(90deg,#9fd4f2 0%,#8fcbef 45%,#7fbfe8 60%,#8d9fd8 78%,#7fa6dc 100%)}
.hero-photo{left:600px;top:62px;width:600px;height:412px;background:radial-gradient(ellipse at 55% 55%,#b08fc7 0%,#9b8fd0 35%,rgba(140,180,230,0) 75%)}
.hero-hey{left:194px;top:155px;font-size:11px;color:var(--blue-mid)}
.hero-title{left:194px;top:178px;font-size:43px;line-height:50px;color:var(--blue-deep);width:290px}
.hero-btn{left:194px;top:354px;width:114px;height:28px;gap:18px;font-weight:500;font-size:10px}

/* offer */
.offer-eyebrow{left:194px;top:560px}
.offer-title{left:194px;top:585px;font-size:27px;line-height:31px;width:380px}
.offer-text{left:194px;top:658px;width:370px;font-size:15px;line-height:19px}
.offer-btn{left:194px;top:770px;width:119px;height:28px}
.faq{left:630px;top:539px;width:376px}
.faq-item{border-top:1px solid var(--blue-mid);height:58px;padding:0 14px;display:flex;align-items:center;justify-content:space-between;font-size:10px;font-weight:500}
.faq-item.open{height:109px;display:block;padding-top:18px}
.faq-item.open .q{display:flex;justify-content:space-between;font-weight:600;margin-bottom:8px}
.faq-item.open p{font-size:8px;line-height:11.5px;color:var(--blue-mid);width:330px}
.faq-item.open a{display:inline-block;margin-top:6px;font-size:8px;font-weight:700;text-decoration:underline;color:var(--blue-deep)}

/* donors */
.donor-eyebrow{left:194px;top:912px}
.donors{left:0;top:975px;width:1200px;height:30px}
.donor{position:absolute;top:0;display:flex;align-items:center;gap:7px;font-size:19px;font-weight:600;color:#333}
.donor i{display:block;width:22px;height:22px;border-radius:50%;background:#555}
.donor.light{color:#aaa}

/* process */
.process-eyebrow{left:0;width:1200px;top:1054px;text-align:center}
.process-title{left:0;width:1200px;top:1076px;text-align:center;font-size:27px}
.process-text{left:0;width:1200px;top:1124px;text-align:center;font-size:15px;line-height:23px}
.stack-back{left:267px;top:1281px;width:665px;height:294px;border-radius:14px;background:#DCE8F3}
.stack-mid{left:308px;top:1240px;width:584px;height:375px;border-radius:14px;background:var(--blue-pale)}
.quote-card{left:328px;top:1199px;width:543px;height:457px;border-radius:14px;background:var(--blue-deep);color:var(--white)}
.quote-text{position:absolute;left:30px;top:42px;width:483px;text-align:center;font-size:25px;line-height:39px}
.quote-author{position:absolute;left:144px;top:365px;display:flex;align-items:center;gap:16px;font-size:15px;font-weight:600}
.quote-author .avatar{width:60px;height:60px;border-radius:6px;background:var(--accent)}
.arrow-prev{left:194px;top:1411px;width:32px;height:32px;background:var(--blue-soft)}
.arrow-next{left:973px;top:1411px;width:32px;height:32px;background:var(--blue-deep)}

/* awards */
.awards{left:0;top:1745px;width:1200px;height:318px;background:var(--blue-deep)}
.badge{position:absolute;top:90px;width:70px;height:70px;border-radius:50%;border:2px solid var(--blue-pale)}
.awards-title{position:absolute;left:0;width:1200px;top:196px;text-align:center;color:var(--white);font-size:31px}

/* work */
.work-eyebrow{left:194px;top:2140px}
.work-title{left:194px;top:2163px;font-size:27px;line-height:31px}
.work-btn{left:194px;top:2257px;width:107px;height:24px}
.work-prev{left:194px;top:2407px;width:31px;height:31px;background:var(--blue-soft)}
.work-next{left:237px;top:2407px;width:31px;height:31px;background:var(--blue-deep)}
.work-card{top:2139px;width:250px}
.work-img{height:155px;border-radius:8px}
.work-meta{display:flex;justify-content:space-between;font-size:9.5px;font-weight:500;margin-top:27px}
.work-card h3{font-size:15.5px;line-height:22px;font-weight:700;margin-top:12px}
.work-card p{font-size:10px;line-height:15px;color:var(--blue-mid);margin-top:8px}

/* cta */
.lower-band{left:0;top:2640px;width:1200px;height:485px;background:var(--blue-deep)}
.cta-box{left:194px;top:2518px;width:812px;height:250px;border-radius:12px;background:var(--blue-pale)}
.cta-title{position:absolute;left:61px;top:48px;font-size:44px}
.cta-text{position:absolute;left:61px;top:110px;width:220px;font-size:10px;line-height:14px}
.cta-btn{position:absolute;left:61px;top:168px;width:188px;height:35px;font-size:11px}
.cta-ring{position:absolute;left:553px;top:27px;width:198px;height:198px;border-radius:50%;border:14px solid var(--blue-soft)}

/* footer */
.footer-col{top:2818px;color:var(--white)}
.footer-col h4{font-size:13px;font-weight:600;margin-bottom:16px}
.footer-col li{list-style:none;font-size:10px;line-height:22.5px}
.footer-col li.current{text-decoration:underline}
.footer-col.bold li{font-weight:600}
.footer-col .loc{font-size:10px;line-height:12px;margin-bottom:14px}
.bottom-bar{left:0;top:3072px;width:1200px;height:53px;background:var(--bar);color:var(--blue-pale);font-size:9.5px}
.bottom-bar span{position:absolute;top:22px}
.social{position:absolute;top:20px;width:13px;height:13px;border-radius:50%;border:1.5px solid var(--blue-pale)}
</style>
</head>
<body>

<header class="abs site-header">
  <div class="abs brand"><span class="brand-dot"></span><span class="brand-name">Harborlight Community<br>Programs</span></div>
  <nav class="abs nav"><span>About</span><span>Work</span><span>Services</span><span>Resources</span><span>Contact</span></nav>
  <div class="abs pill solid cta-top">Let's collaborate
    <span class="circle-btn"><svg width="9" height="9" viewBox="0 0 10 10"><path d="M1 5h8M5.5 1.5L9 5 5.5 8.5" fill="none" stroke="#fff" stroke-width="1.2"/></svg></span>
  </div>
</header>

<section>
  <div class="abs hero"></div>
  <div class="abs hero-photo" role="img" aria-label="Cupped hands holding a heart made of colourful puzzle pieces"></div>
  <p class="abs hero-hey">Hey! We're&nbsp; !</p>
  <h1 class="abs serif hero-title">Empowering Lives, Building Communities</h1>
  <div class="abs pill solid hero-btn">Learn More
    <svg width="11" height="11" viewBox="0 0 10 10"><path d="M1 5h8M5.5 1.5L9 5 5.5 8.5" fill="none" stroke="#fff" stroke-width="1.2"/></svg>
  </div>
</section>

<section>
  <p class="abs eyebrow offer-eyebrow">• What we offer</p>
  <h2 class="abs serif offer-title">Intellectual &amp; Developmental Disabilities</h2>
  <p class="abs offer-text">Harborlight Community Programs provides compassionate care for adults with intellectual and developmental disabilities, autism, mental health challenges, and substance abuse issues.</p>
  <div class="abs pill soft offer-btn">See our Services</div>

  <div class="abs faq">
    <div class="faq-item"><span>Are you in-network with my health insurance?</span><svg width="8" height="11" viewBox="0 0 8 11"><path d="M1.5 1l5 4.5-5 4.5" fill="none" stroke="#0054AA" stroke-width="1.2"/></svg></div>
    <div class="faq-item open">
      <div class="q"><span>Where is location?</span><svg width="12" height="8" viewBox="0 0 12 8"><path d="M1 1.5l5 5 5-5" fill="none" stroke="#0054AA" stroke-width="1.2"/></svg></div>
      <p>We have locations throughout the United States, and we offer care in the clinic, at your home or by telehealth, depending on your location and insurance coverage. Please visit our Where to Find Us page to see our locations.</p>
      <a>LEARN MORE</a>
    </div>
    <div class="faq-item"><span>What ages do you accept?</span><svg width="8" height="11" viewBox="0 0 8 11"><path d="M1.5 1l5 4.5-5 4.5" fill="none" stroke="#0054AA" stroke-width="1.2"/></svg></div>
    <div class="faq-item"><span>What services do you offer?</span><svg width="8" height="11" viewBox="0 0 8 11"><path d="M1.5 1l5 4.5-5 4.5" fill="none" stroke="#0054AA" stroke-width="1.2"/></svg></div>
    <div class="faq-item"><span>Do you only provide care for autism?</span><svg width="8" height="11" viewBox="0 0 8 11"><path d="M1.5 1l5 4.5-5 4.5" fill="none" stroke="#0054AA" stroke-width="1.2"/></svg></div>
  </div>
</section>

<section>
  <p class="abs eyebrow donor-eyebrow">• Our donors</p>
  <div class="abs donors">
    <div class="donor" style="left:-20px">Brightleaf</div>
    <div class="donor" style="left:152px"><i></i>nestwave</div>
    <div class="donor" style="left:344px"><i></i>ThinkRiver</div>
    <div class="donor" style="left:536px"><i></i>LedgerPal</div>
    <div class="donor light" style="left:714px">Candytide</div>
    <div class="donor" style="left:892px"><i></i>quickstudy</div>
    <div class="donor light" style="left:1140px"><i></i>orvia</div>
  </div>
</section>

<section>
  <p class="abs eyebrow process-eyebrow">• Our process</p>
  <h2 class="abs serif process-title">You'll be so proud of their progress</h2>
  <p class="abs process-text">Every day we see children soar to new heights. Here are some of their<br>stories — as told by the people who love them.</p>
  <div class="abs stack-back"></div>
  <div class="abs stack-mid"></div>
  <figure class="abs quote-card">
    <blockquote class="quote-text">“The Harborlight Community Programs team has exceeded my expectations. What sets them apart from other behavioral companies is they have a highly trained group of knowledgeable professionals working together as a team all under one roof.”</blockquote>
    <figcaption class="quote-author"><span class="avatar"></span>–Mom of seven-year-old</figcaption>
  </figure>
  <div class="abs circle-btn arrow-prev"><svg width="13" height="13" viewBox="0 0 10 10"><path d="M9 5H1M4.5 1.5L1 5l3.5 3.5" fill="none" stroke="#fff" stroke-width="1"/></svg></div>
  <div class="abs circle-btn arrow-next"><svg width="13" height="13" viewBox="0 0 10 10"><path d="M1 5h8M5.5 1.5L9 5 5.5 8.5" fill="none" stroke="#fff" stroke-width="1"/></svg></div>
</section>

<section class="abs awards">
  <span class="badge" style="left:276px"></span>
  <span class="badge" style="left:468px"></span>
  <span class="badge" style="left:660px"></span>
  <span class="badge" style="left:853px"></span>
  <h2 class="serif awards-title">Industry leaders recognise our excellence</h2>
</section>

<section>
  <p class="abs eyebrow work-eyebrow">• Our work</p>
  <h2 class="abs serif work-title">We care for the<br>whole child</h2>
  <div class="abs pill soft work-btn">View our work</div>
  <div class="abs circle-btn work-prev"><svg width="13" height="13" viewBox="0 0 10 10"><path d="M9 5H1M4.5 1.5L1 5l3.5 3.5" fill="none" stroke="#fff" stroke-width="1"/></svg></div>
  <div class="abs circle-btn work-next"><svg width="13" height="13" viewBox="0 0 10 10"><path d="M1 5h8M5.5 1.5L9 5 5.5 8.5" fill="none" stroke="#fff" stroke-width="1"/></svg></div>

  <article class="abs work-card" style="left:444px">
    <div class="work-img" role="img" aria-label="Group of older adults laughing together on a sofa" style="background:linear-gradient(135deg,#d9d4cc,#b7b9c0 50%,#8f9fb6)"></div>
    <div class="work-meta"><span>Communication</span><span>2024</span></div>
    <h3>Lorem ipsum dolor sit amet, dolor sit amet, dolor sit amet</h3>
    <p>Lorem ipsum dolor sit amet, consectetuer adipiscing elit, sed diam nonummy nibh euismod tincidunt ut laoreet dolore magna ali</p>
  </article>
  <article class="abs work-card" style="left:756px">
    <div class="work-img" role="img" aria-label="Family sharing a meal at a kitchen table" style="background:linear-gradient(135deg,#6b5a4c,#b49a84 45%,#e2ddd6)"></div>
    <div class="work-meta"><span>Social skills</span><span>2024</span></div>
    <h3>Lorem ipsum dolor sit amet, dolor sit amet, dolor sit amet</h3>
    <p>Lorem ipsum dolor sit amet, consectetuer adipiscing elit, sed diam nonummy nibh euismod tincidunt ut laoreet dolore magna ali</p>
  </article>
</section>

<div class="abs lower-band"></div>
<section class="abs cta-box">
  <h2 class="serif cta-title">Together, we can unlock</h2>
  <p class="cta-text">Lorem ipsum dolor sit amet, consectetuer adipiscing elit, sed diam nonummy nibh</p>
  <div class="pill solid cta-btn">Get Make An Appointment</div>
  <span class="cta-ring"></span>
</section>

<footer>
  <div class="abs footer-col" style="left:194px">
    <h4>Explore</h4>
    <ul><li class="current">Home</li><li>Work</li><li>Services</li><li>Careers</li><li>Contact</li><li>Blog</li><li>FAQs</li></ul>
  </div>
  <div class="abs footer-col bold" style="left:394px">
    <h4>Services</h4>
    <ul><li>Intellectual Developmental Disabilities</li><li>Group Homes,</li><li>Residential Homes</li><li>Substance Abuse Residential facilities</li></ul>
  </div>
  <div class="abs footer-col" style="left:644px">
    <h4>Get in touch</h4>
    <ul><li>hi@harborlightcommunity.org</li><li style="margin-top:3px">0800 555 010203</li><li>0800 555 010203</li></ul>
  </div>
  <div class="abs footer-col" style="left:887px;top:2821px">
    <h4>Locations</h4>
    <p class="loc">Coastal Region Pier Point,<br>Eastmere</p>
    <p class="loc">Inland Region&nbsp; Millbrook,<br><b>Westvale</b></p>
  </div>
  <div class="abs bottom-bar">
    <span style="left:194px">© Harborlight Community Programs 2025</span>
    <span style="left:502px">All Rights Reserved</span>
    <span style="left:613px">|</span>
    <span style="left:633px">Privacy Policy</span>
    <i class="social" style="left:915px"></i>
    <i class="social" style="left:940px"></i>
    <i class="social" style="left:965px"></i>
    <i class="social" style="left:993px"></i>
  </div>
</footer>

</body>
</html>
```